SKILLSTEP is a training facility that offers training or entry level positions in the oil and gas i

We are needing a business card design for a new business called SKILLSTEP Industry training Inc. We are a training facility offering courses for entry level positions in the oil and gas industry. We like to keep the design in the colours of our logo. we like this also on the card "Get Prepared For A Flexible Career You Can Build On"

Industry/Entity Type

Oil And Gas

Contact Information for Business Card

Dorian Wexley
RR3 Site 9 Comp27
Fort St. John, BC, V2K8P3
250.418.5069 cell
250.418.7312 office
dorian@SKILLSTEPNORTH.ca
WWW.SKILLSTEPNORTH.CA

```html
<!DOCTYPE html>
<html lang="en">
<head>
<meta charset="utf-8">
<title>SKILLSTEP Industry Training Inc. – Business Card</title>
<link rel="stylesheet" href="https://fonts.googleapis.com/css2?family=Arimo:wght@400&family=Open+Sans:wght@600;700&display=swap">
<style>
  :root {
    --bg: #d9d9d9;
    --card: #ffffff;
    --ink: #111111;
    --brand-grey: #6b6b6b;
    --brand-orange: #ef7a2a;
    --brand-blue: #12a6d8;
    --brand-blue-deep: #0e94cf;
  }
  * { box-sizing: border-box; margin: 0; padding: 0; }
  html, body { width: 1200px; height: 864px; overflow: hidden; }
  body {
    background: var(--bg);
    display: flex;
    align-items: center;
    justify-content: center;
    gap: 60px;
  }
  .card {
    position: relative;
    width: 520px;
    height: 330px;
    background: var(--card);
    box-shadow: 0 6px 18px rgba(0,0,0,0.18);
    overflow: hidden;
  }
  .card__wave {
    position: absolute;
    left: 0; bottom: 0;
    width: 520px; height: 330px;
  }
  .brand {
    position: absolute;
    display: flex;
    align-items: center;
    gap: 16px;
    font-family: "Open Sans", sans-serif;
    font-weight: 700;
    color: var(--brand-grey);
  }
  .brand__dot {
    border-radius: 50%;
    background: var(--brand-orange);
    flex: none;
  }
  .brand__name { line-height: 1.05; }
  .brand__name span { display: block; letter-spacing: 0.04em; }
  .brand--front { left: 100px; top: 78px; }
  .brand--front .brand__dot { width: 60px; height: 60px; }
  .brand--front .brand__main { font-size: 44px; }
  .brand--front .brand__sub { font-size: 13px; letter-spacing: 0.12em; margin-top: 4px; }

  .brand--contact { left: 34px; top: 26px; gap: 12px; }
  .brand--contact .brand__dot { width: 38px; height: 38px; }
  .brand--contact .brand__main { font-size: 27px; }
  .brand--contact .brand__sub { font-size: 8.5px; letter-spacing: 0.12em; margin-top: 2px; }

  .contact {
    position: absolute;
    left: 34px;
    top: 92px;
    list-style: none;
    font-family: "Arimo", sans-serif;
    font-size: 13px;
    color: var(--ink);
  }
  .contact__item {
    display: flex;
    align-items: flex-start;
    gap: 12px;
    margin-bottom: 7px;
    line-height: 1.25;
  }
  .contact__icon { width: 14px; height: 14px; flex: none; margin-top: 1px; }
</style>
</head>
<body>

  <section class="card card--front" aria-label="Card front">
    <div class="brand brand--front">
      <div class="brand__dot"></div>
      <div class="brand__name">
        <span class="brand__main">SKILLSTEP</span>
        <span class="brand__sub">INDUSTRY TRAINING INC.</span>
      </div>
    </div>
    <svg class="card__wave" viewBox="0 0 520 330" aria-hidden="true">
      <path d="M0,212 C140,196 270,206 380,250 C440,274 490,282 520,282 L520,330 L0,330 Z" fill="var(--brand-orange)"/>
      <path d="M0,220 C140,204 270,214 380,258 C440,282 490,290 520,290 L520,330 L0,330 Z" fill="var(--brand-blue)"/>
    </svg>
  </section>

  <section class="card card--contact" aria-label="Card back">
    <div class="brand brand--contact">
      <div class="brand__dot"></div>
      <div class="brand__name">
        <span class="brand__main">SKILLSTEP</span>
        <span class="brand__sub">INDUSTRY TRAINING INC.</span>
      </div>
    </div>

    <ul class="contact">
      <li class="contact__item">
        <svg class="contact__icon" viewBox="0 0 14 14" aria-hidden="true"><path d="M7,0.5 C4.2,0.5 2.5,2.5 2.5,4.8 C2.5,8 7,13.5 7,13.5 C7,13.5 11.5,8 11.5,4.8 C11.5,2.5 9.8,0.5 7,0.5 Z M7,6.5 A1.7,1.7 0 1 1 7,3.1 A1.7,1.7 0 1 1 7,6.5 Z" fill="var(--ink)"/></svg>
        <span>Dorian Wexley RR3 Site 9 Comp27 Fort St.<br>John, BC, V2K8P3</span>
      </li>
      <li class="contact__item">
        <svg class="contact__icon" viewBox="0 0 14 14" aria-hidden="true"><rect x="3.5" y="0.5" width="7" height="13" rx="1" fill="none" stroke="var(--ink)" stroke-width="1.2"/><rect x="5" y="2.2" width="4" height="4" fill="var(--ink)"/><circle cx="7" cy="11" r="0.9" fill="var(--ink)"/></svg>
        <span>250.418.5069</span>
      </li>
      <li class="contact__item">
        <svg class="contact__icon" viewBox="0 0 14 14" aria-hidden="true"><path d="M3.5,1 L5.5,1 L6,4.5 L4.6,5.4 C5.3,7.3 6.7,8.7 8.6,9.4 L9.5,8 L13,8.5 L13,10.5 C13,12 11.8,13 10.3,12.8 C5.8,12.2 1.8,8.2 1.2,3.7 C1,2.2 2,1 3.5,1 Z" fill="var(--ink)"/></svg>
        <span>250.418.7312</span>
      </li>
      <li class="contact__item">
        <svg class="contact__icon" viewBox="0 0 14 14" aria-hidden="true"><rect x="0.5" y="2.5" width="13" height="9" fill="var(--ink)"/><path d="M0.8,2.8 L7,7.6 L13.2,2.8" fill="none" stroke="var(--card)" stroke-width="1"/></svg>
        <span>dorian@SKILLSTEPNORTH.ca</span>
      </li>
      <li class="contact__item">
        <svg class="contact__icon" viewBox="0 0 14 14" aria-hidden="true"><g fill="none" stroke="var(--ink)" stroke-width="1"><circle cx="7" cy="7" r="6"/><ellipse cx="7" cy="7" rx="2.6" ry="6"/><path d="M1,7 L13,7 M2,4 L12,4 M2,10 L12,10"/></g></svg>
        <span>WWW.SKILLSTEPNORTH.CA</span>
      </li>
    </ul>

    <svg class="card__wave" viewBox="0 0 520 330" aria-hidden="true">
      <path d="M0,226 C140,210 270,222 380,262 C440,284 490,292 520,292 L520,330 L0,330 Z" fill="var(--brand-orange)"/>
      <path d="M0,234 C140,218 270,230 380,270 C440,292 490,300 520,300 L520,330 L0,330 Z" fill="var(--brand-blue)"/>
    </svg>
  </section>

</body>
</html>
```